Designing a website for Brightmoor Pest Services PTY LTD

Pest control company looking for someone to build an informative website containing services we offer and an online inquiry form.
Commercial premises - Specialising in - Rodent control, stored product pest control, flying insect control, ant, spider and insect control, Termite inspections and treatments. Termite management systems on a commercial scale.
Facilities we service
Commercial - shopping centres, transport facilities, restaurants, pubs, clubs, bars food manufacturing facilities.
Residential - Houses specialising in - Rodent, Ant, Spider, Cockroach and Termite control. Termite inspections, Pre - purchase inspections, Termite treatments, Termite management systems.
Target Market(s)
Mainly commercial and industrial clients and Residential clients.
Industry/Entity Type
Pest Control
Number of Pages Required
1 page
Look and feel

```html
<!DOCTYPE html>
<html lang="en">
<head>
<meta charset="utf-8">
<title>Brightmoor Pest Services PTY LTD</title>
<link rel="stylesheet" href="https://fonts.googleapis.com/css2?family=Montserrat:wght@400;500;600;700&display=swap">
<style>
:root{
  --green:#2f8a12;
  --green-dark:#257009;
  --ink:#1d1d1d;
  --text:#3a3a3a;
  --muted:#555;
  --white:#fff;
  --dark:#0b0b0b;
  --footer:#f3f3f3;
  --bar:#c8654c;
  --red:#e04848;
  --gold:#f4c20d;
}
*{box-sizing:border-box;margin:0;padding:0}
html,body{width:1200px;height:2805px;overflow:hidden}
body{font-family:'Montserrat',sans-serif;color:var(--text);background:var(--white);position:relative}
.page{position:relative;width:1200px;height:2805px;overflow:hidden}
a{text-decoration:none;color:inherit}

/* header */
.site-header{position:absolute;top:0;left:0;width:1200px;height:149px;background:var(--white);box-shadow:0 3px 8px rgba(0,0,0,.18);z-index:5}
.brand{position:absolute;left:112px;top:52px;display:flex;align-items:center;gap:10px;font-weight:700;font-size:32px;color:var(--ink);letter-spacing:-.5px}
.brand-dot{width:22px;height:22px;border-radius:50%;background:var(--green)}
.contact-item{position:absolute;top:26px;display:flex;gap:12px;align-items:flex-start;white-space:nowrap}
.contact-item .label{font-size:14px;color:var(--ink);font-weight:500}
.contact-item .value{font-size:18px;color:var(--green);font-weight:600;margin-top:2px}
.contact-item svg{margin-top:6px}
.main-nav{position:absolute;top:93px;right:292px;display:flex;gap:16px;font-size:14px;font-weight:500;color:var(--ink);white-space:nowrap}
.main-nav .active{color:var(--green)}
.quote-btn{position:absolute;left:925px;top:85px;width:162px;height:34px;border-radius:17px;background:var(--green);color:var(--white);font-size:12.5px;font-weight:600;letter-spacing:3px;display:flex;align-items:center;justify-content:center}

/* hero */
.hero{position:absolute;top:149px;left:0;width:1200px;height:760px}
.hero-photo{position:absolute;inset:0;background:linear-gradient(180deg,#f1f1ef 0%,#e6e4e0 45%,#b9b0a4 75%,#6d5c4f 100%)}
.hero-curve{position:absolute;left:0;top:0}
.hero-content{position:absolute;left:0;top:348px;width:1200px;text-align:center}
.hero-kicker{font-size:21px;letter-spacing:9px;color:var(--ink);font-weight:500}
.hero-title{font-size:44px;font-weight:700;color:var(--ink);margin-top:12px}
.hero-btn{display:inline-flex;align-items:center;justify-content:center;width:171px;height:43px;border-radius:22px;background:var(--green);color:var(--white);font-size:16px;letter-spacing:3px;font-weight:500;margin-top:10px}
.hero-dots{display:flex;justify-content:center;gap:5px;margin-top:14px}
.hero-dots span{width:14px;height:14px;border-radius:50%;border:2px solid var(--white)}
.hero-dots span.on{background:var(--green);border-color:var(--green)}

/* facilities */
.facilities{position:absolute;top:960px;left:109px;width:982px}
.facilities-label{position:absolute;left:0;top:4px;font-size:17.5px;color:var(--green);font-weight:500}
.facilities-title{position:absolute;left:2px;top:36px;width:440px;font-size:31px;line-height:39px;font-weight:600;color:#444}
.facilities-text{position:absolute;left:490px;top:0;width:500px;font-size:15.8px;line-height:25px;color:#444}
.cards{position:absolute;top:1143px;left:110px;display:flex}
.card{display:flex;height:377px;width:490px;box-shadow:0 0 8px rgba(0,0,0,.12)}
.card-photo{width:245px;height:100%}
.photo-city{background:linear-gradient(160deg,#2d4a88 0%,#6d8ac0 45%,#2a3f6b 100%)}
.photo-pest{background:linear-gradient(170deg,#efe4dc 0%,#b08d70 45%,#5a4030 75%,#9c9a96 100%)}
.card-body{width:245px;background:var(--white);padding:22px 15px 0 15px}
.card-head{display:flex;align-items:center;gap:14px;font-size:22px;font-weight:500;color:#444}
.card-list{list-style:none;margin-top:26px}
.card-list li{display:flex;gap:10px;font-size:14.5px;color:#333;line-height:18px;margin-bottom:12px}
.card-list svg{flex:none;margin-top:2px}
.read-more{display:flex;align-items:center;gap:6px;font-size:13px;color:var(--green);font-weight:500;margin:22px 0 0 6px}

/* welcome */
.welcome{position:absolute;top:1588px;left:0;width:1200px;height:445px;background:var(--dark)}
.welcome-photo{position:absolute;left:54px;top:0;width:1076px;height:445px;background:linear-gradient(120deg,#1b1c1c 0%,#262727 40%,#1a1a1a 70%,#2a2b2b 100%)}
.welcome-content{position:absolute;left:0;top:58px;width:1200px;text-align:center;color:var(--white)}
.welcome-kicker{font-size:19px;letter-spacing:5px;font-weight:400}
.welcome-title{font-size:26px;font-weight:600;margin-top:12px}
.rule{display:block;width:86px;height:4px;background:var(--green);margin:14px auto 0}
.welcome-text{width:715px;margin:20px auto 0;font-size:16.5px;line-height:25.5px;color:#e8e8e8}
.welcome-actions{display:flex;justify-content:center;gap:15px;margin-top:24px}
.pill{width:163px;height:33px;border-radius:17px;display:flex;align-items:center;justify-content:center;gap:8px;font-size:13px;letter-spacing:3px;font-weight:600;color:var(--white)}
.pill.solid{background:var(--green)}
.pill.outline{border:2px solid var(--white)}

/* testimonial */
.testimonial{position:absolute;top:2033px;left:0;width:1200px;height:489px}
.client-photo{position:absolute;left:112px;top:118px;width:250px;height:250px;border-radius:50%;background:radial-gradient(circle at 45% 40%,#e9d6c4 0%,#b99278 45%,#6b5240 100%)}
.quote-mark{position:absolute;left:160px;top:300px;font-size:150px;line-height:1;font-weight:700;color:var(--green);font-family:Georgia,serif}
.testimonial-body{position:absolute;left:409px;top:70px;width:650px}
.testimonial-kicker{font-size:19px;letter-spacing:5px;color:var(--ink)}
.testimonial-title{font-size:27px;font-weight:600;color:var(--ink);margin-top:12px}
.testimonial-body .rule{margin:12px 0 0 0}
.testimonial-text{font-size:13.5px;line-height:22.3px;color:#333;margin-top:22px}
.client-name{font-size:18px;color:var(--ink);margin-top:18px;font-weight:500}
.client-name span{margin-right:22px}
.stars{display:flex;gap:2px;margin-top:6px}
.slider-nav{display:flex;gap:19px;margin-top:12px}
.slider-nav span{width:41px;height:41px;background:#000;display:flex;align-items:center;justify-content:center}

/* footer */
.site-footer{position:absolute;top:2522px;left:0;width:1200px;height:244px;background:var(--footer);border-top:1px solid #9a9a9a}
.footer-brand{position:absolute;left:112px;top:58px;display:flex;align-items:center;gap:8px;font-size:26px;font-weight:700;color:var(--ink)}
.footer-brand span{width:16px;height:16px;border-radius:50%;background:var(--green)}
.social{position:absolute;left:136px;top:147px;display:flex;gap:13px}
.social span{width:28px;height:28px;border-radius:50%;background:#000}
.footer-col{position:absolute;top:53px}
.footer-col::before{content:"";display:block;width:38px;height:4px;background:var(--green);margin-bottom:14px}
.footer-col h4{font-size:17.5px;font-weight:500;color:#444;letter-spacing:.5px}
.touch{left:313px;width:215px}
.touch ul{list-style:none;margin-top:12px}
.touch li{display:flex;gap:16px;font-size:14px;line-height:21px;font-weight:500;color:#333;margin-bottom:7px;white-space:nowrap}
.touch svg{flex:none;margin-top:4px}
.links{left:542px}
.links ul{list-style:none;margin-top:14px;font-size:12.5px;line-height:20.5px;color:#444}
.signup{left:715px}
.signup .field{width:241px;height:34px;border-radius:17px;background:var(--white);box-shadow:0 1px 4px rgba(0,0,0,.2);margin-top:12px;font-size:12.5px;color:#555;padding:9px 0 0 20px}
.signup .submit{width:241px;height:34px;border-radius:17px;background:var(--green);color:var(--white);font-size:13px;font-weight:600;letter-spacing:3.5px;margin-top:13px;display:flex;align-items:center;justify-content:center}
.footer-art{position:absolute;left:942px;top:31px;width:258px;height:213px;background:radial-gradient(ellipse at 55% 45%,#d9d9d9 0%,#bdbdbd 40%,rgba(210,90,70,.35) 75%,rgba(243,243,243,0) 100%)}
.copyright{position:absolute;top:2766px;left:0;width:1200px;height:39px;background:var(--bar);color:#3a2320;font-size:12px;display:flex;align-items:center;justify-content:center}
</style>
</head>
<body>
<div class="page">

<header class="site-header">
  <div class="brand"><span class="brand-dot"></span>Brightmoor</div>
  <div class="contact-item" style="left:651px">
    <svg width="30" height="30" viewBox="0 0 24 24"><path fill="#2f8a12" d="M6.6 10.8a15.1 15.1 0 0 0 6.6 6.6l2.2-2.2c.3-.3.7-.4 1-.2 1.1.4 2.3.6 3.6.6.6 0 1 .4 1 1V20c0 .6-.4 1-1 1A17 17 0 0 1 3 4c0-.6.4-1 1-1h3.5c.6 0 1 .4 1 1 0 1.3.2 2.5.6 3.6.1.3 0 .7-.2 1z"/></svg>
    <div><div class="label">Need A Help?</div><div class="value">620-555-0147</div></div>
  </div>
  <div class="contact-item" style="left:862px">
    <svg width="30" height="24" viewBox="0 0 30 22"><path fill="#2f8a12" d="M0 2a2 2 0 0 1 2-2h26a2 2 0 0 1 2 2v1L15 12 0 3z"/><path fill="#2f8a12" d="M0 6l15 9 15-9v14a2 2 0 0 1-2 2H2a2 2 0 0 1-2-2z"/></svg>
    <div><div class="label">Email To</div><div class="value">info@brightmoor.com</div></div>
  </div>
  <nav class="main-nav">
    <a class="active">Home</a><a>About Us</a><a>What We Do</a><a>Commercial</a><a>Residential</a><a>Contact Us</a>
  </nav>
  <a class="quote-btn">GET A QUOTE</a>
</header>

<section class="hero">
  <div class="hero-photo" role="img" aria-label="Two technicians in white protective suits spraying pest treatment in a bright living room"></div>
  <svg class="hero-curve" width="1200" height="760" viewBox="0 0 1200 760">
    <path fill="#2f8a12" d="M0 600 Q380 800 1200 430 L1200 442 Q420 875 0 700 Z"/>
    <path fill="#ffffff" d="M0 700 Q420 875 1200 442 L1200 760 L0 760 Z"/>
  </svg>
  <div class="hero-content">
    <div class="hero-kicker">WELCOME TO</div>
    <h1 class="hero-title">Brightmoor Pest Services PTY LTD</h1>
    <a class="hero-btn">Get Started</a>
    <div class="hero-dots"><span class="on"></span><span></span><span></span></div>
  </div>
</section>

<section class="facilities">
  <div class="facilities-label">Facilities we service</div>
  <h2 class="facilities-title">Neque porro Quisquam est qui dolorem ipsum quia dolor sit amet.</h2>
  <p class="facilities-text">Commercial premises - Specialising in - Rodent control, stored product pest control, flying insect control, ant, spider and insect control, Termite inspections and treatments. Termite management systems on a commercial scale.</p>
</section>

<div class="cards">
  <article class="card">
    <div class="card-photo photo-city" role="img" aria-label="Glass office towers viewed from below"></div>
    <div class="card-body">
      <div class="card-head">
        <svg width="42" height="56" viewBox="0 0 42 56" fill="none" stroke="#777" stroke-width="1.6"><rect x="4" y="8" width="34" height="46"/><rect x="10" y="2" width="22" height="6"/><path d="M10 16h6M19 16h5M27 16h5M10 24h6M19 24h5M27 24h5M10 32h6M19 32h5M27 32h5M10 40h6M19 40h5M27 40h5M17 54v-8h8v8"/></svg>
        Commercial
      </div>
      <ul class="card-list">
        <li><svg width="14" height="14" viewBox="0 0 14 14"><path fill="#e04848" d="M7 0l6 2.5v4C13 10 10 13 7 14 4 13 1 10 1 6.5v-4z"/><circle cx="7" cy="6.5" r="2.3" fill="#fff"/></svg>Shopping Centers</li>
        <li><svg width="14" height="14" viewBox="0 0 14 14"><path fill="#e04848" d="M7 0l6 2.5v4C13 10 10 13 7 14 4 13 1 10 1 6.5v-4z"/><circle cx="7" cy="6.5" r="2.3" fill="#fff"/></svg>Transport Facilities</li>
        <li><svg width="14" height="14" viewBox="0 0 14 14"><path fill="#e04848" d="M7 0l6 2.5v4C13 10 10 13 7 14 4 13 1 10 1 6.5v-4z"/><circle cx="7" cy="6.5" r="2.3" fill="#fff"/></svg>Restaurants</li>
        <li><svg width="14" height="14" viewBox="0 0 14 14"><path fill="#e04848" d="M7 0l6 2.5v4C13 10 10 13 7 14 4 13 1 10 1 6.5v-4z"/><circle cx="7" cy="6.5" r="2.3" fill="#fff"/></svg>Pubs</li>
        <li><svg width="14" height="14" viewBox="0 0 14 14"><path fill="#e04848" d="M7 0l6 2.5v4C13 10 10 13 7 14 4 13 1 10 1 6.5v-4z"/><circle cx="7" cy="6.5" r="2.3" fill="#fff"/></svg>Clubs</li>
        <li><svg width="14" height="14" viewBox="0 0 14 14"><path fill="#e04848" d="M7 0l6 2.5v4C13 10 10 13 7 14 4 13 1 10 1 6.5v-4z"/><circle cx="7" cy="6.5" r="2.3" fill="#fff"/></svg>Bars</li>
        <li><svg width="14" height="14" viewBox="0 0 14 14"><path fill="#e04848" d="M7 0l6 2.5v4C13 10 10 13 7 14 4 13 1 10 1 6.5v-4z"/><circle cx="7" cy="6.5" r="2.3" fill="#fff"/></svg>Food Manufacturing Facilities</li>
      </ul>
      <a class="read-more">Read More <svg width="12" height="11" viewBox="0 0 12 11"><path d="M0 5.5h10M6 1l4.5 4.5L6 10" stroke="#2f8a12" stroke-width="2" fill="none"/></svg></a>
    </div>
  </article>
  <article class="card">
    <div class="card-photo photo-pest" role="img" aria-label="Fingers holding a cockroach above a kitchen drain"></div>
    <div class="card-body">
      <div class="card-head">
        <svg width="46" height="44" viewBox="0 0 46 44" fill="none" stroke="#777" stroke-width="1.6"><path d="M2 22L23 3l21 19M8 17v25h30V17M33 9V4h5v10"/><rect x="12" y="26" width="9" height="16"/><rect x="25" y="26" width="9" height="9"/><path d="M29.5 26v9M25 30.5h9"/></svg>
        Residential
      </div>
      <ul class="card-list">
        <li><svg width="14" height="14" viewBox="0 0 14 14"><path fill="#e04848" d="M7 0l6 2.5v4C13 10 10 13 7 14 4 13 1 10 1 6.5v-4z"/><circle cx="7" cy="6.5" r="2.3" fill="#fff"/></svg>Rodent, Ant,</li>
        <li><svg width="14" height="14" viewBox="0 0 14 14"><path fill="#e04848" d="M7 0l6 2.5v4C13 10 10 13 7 14 4 13 1 10 1 6.5v-4z"/><circle cx="7" cy="6.5" r="2.3" fill="#fff"/></svg>Termite control</li>
        <li><svg width="14" height="14" viewBox="0 0 14 14"><path fill="#e04848" d="M7 0l6 2.5v4C13 10 10 13 7 14 4 13 1 10 1 6.5v-4z"/><circle cx="7" cy="6.5" r="2.3" fill="#fff"/></svg>Cockroach</li>
        <li><svg width="14" height="14" viewBox="0 0 14 14"><path fill="#e04848" d="M7 0l6 2.5v4C13 10 10 13 7 14 4 13 1 10 1 6.5v-4z"/><circle cx="7" cy="6.5" r="2.3" fill="#fff"/></svg>Spider</li>
        <li><svg width="14" height="14" viewBox="0 0 14 14"><path fill="#e04848" d="M7 0l6 2.5v4C13 10 10 13 7 14 4 13 1 10 1 6.5v-4z"/><circle cx="7" cy="6.5" r="2.3" fill="#fff"/></svg>Termite Treatments</li>
        <li><svg width="14" height="14" viewBox="0 0 14 14"><path fill="#e04848" d="M7 0l6 2.5v4C13 10 10 13 7 14 4 13 1 10 1 6.5v-4z"/><circle cx="7" cy="6.5" r="2.3" fill="#fff"/></svg>Termite Management</li>
        <li><svg width="14" height="14" viewBox="0 0 14 14"><path fill="#e04848" d="M7 0l6 2.5v4C13 10 10 13 7 14 4 13 1 10 1 6.5v-4z"/><circle cx="7" cy="6.5" r="2.3" fill="#fff"/></svg>Termite inspections</li>
      </ul>
      <a class="read-more" style="margin-top:40px">Read More <svg width="12" height="11" viewBox="0 0 12 11"><path d="M0 5.5h10M6 1l4.5 4.5L6 10" stroke="#2f8a12" stroke-width="2" fill="none"/></svg></a>
    </div>
  </article>
</div>

<section class="welcome">
  <div class="welcome-photo" role="img" aria-label="Dimly lit photo of a technician at work, used as a dark backdrop"></div>
  <div class="welcome-content">
    <div class="welcome-kicker">WELCOME TO</div>
    <h2 class="welcome-title">BRIGHTMOOR PEST SERVICES PTY LTD</h2>
    <span class="rule"></span>
    <p class="welcome-text">Lorem Ipsum is simply dummy text of the printing and typesetting industry. Lorem Ipsum has been the industry's standard dummy text ever since the 1500s, when an unknown printer took a galley of type and scrambled it to make a type specimen book. It has survived not only five centuries, but also the leap into electronic typesetting, remaining essentially unchanged. It was popularised in the 1960s with the release of Letraset sheets containing Lorem Ipsum passages, and more recently with desktop publishing software like Aldus PageMaker including versions of Lorem Ipsum.</p>
    <div class="welcome-actions">
      <a class="pill solid">READ MORE <svg width="12" height="11" viewBox="0 0 12 11"><path d="M0 5.5h10M6 1l4.5 4.5L6 10" stroke="#fff" stroke-width="2" fill="none"/></svg></a>
      <a class="pill outline">FREE QUOTE <svg width="12" height="11" viewBox="0 0 12 11"><path d="M0 5.5h10M6 1l4.5 4.5L6 10" stroke="#fff" stroke-width="2" fill="none"/></svg></a>
    </div>
  </div>
</section>

<section class="testimonial">
  <div class="client-photo" role="img" aria-label="Family gathered around a laptop on a sofa"></div>
  <div class="quote-mark">&ldquo;</div>
  <div class="testimonial-body">
    <div class="testimonial-kicker">WHAT OUR</div>
    <h2 class="testimonial-title">HAPPY CLIENTS SAY ABOUT US</h2>
    <span class="rule"></span>
    <p class="testimonial-text">“Lorem Ipsum is simply dummy text of the printing and typesetting industry. Lorem Ipsum has been the industry's standard dummy text ever since the 1500s, when an unknown printer took a galley of type and scrambled it to make a type specimen book. It has survived not only five centuries, but also the leap into electronic typesetting, remaining essentially unchanged. It was popularised in the 1960s with the release of Letraset sheets containing”</p>
    <div class="client-name"><span>-</span>Joanna M Keller</div>
    <div class="stars">
      <svg width="130" height="25" viewBox="0 0 130 25"><g fill="#f4c20d"><path id="st" d="M12.5 0l3 8.5H25l-7.5 5.5 3 9-8-5.5-8 5.5 3-9L0 8.5h9.5z"/><use href="#st" x="26"/><use href="#st" x="52"/><use href="#st" x="78"/><use href="#st" x="104"/></g></svg>
    </div>
    <div class="slider-nav">
      <span><svg width="14" height="22" viewBox="0 0 14 22"><path d="M12 2L3 11l9 9" stroke="#fff" stroke-width="3" fill="none"/></svg></span>
      <span><svg width="14" height="22" viewBox="0 0 14 22"><path d="M2 2l9 9-9 9" stroke="#fff" stroke-width="3" fill="none"/></svg></span>
    </div>
  </div>
</section>

<footer class="site-footer">
  <div class="footer-brand"><span></span>Brightmoor</div>
  <div class="social"><span></span><span></span><span></span></div>
  <div class="footer-col touch">
    <h4>GET IN TOUCH</h4>
    <ul>
      <li><svg width="12" height="16" viewBox="0 0 12 16"><path fill="#2f8a12" d="M6 0a6 6 0 0 1 6 6c0 4.5-6 10-6 10S0 10.5 0 6a6 6 0 0 1 6-6z"/><circle cx="6" cy="6" r="2.2" fill="#f3f3f3"/></svg><span>42 Larkspur Avenue,<br>Fairview City,<br>Oklahoma, 73190.</span></li>
      <li><svg width="14" height="14" viewBox="0 0 24 24"><path fill="#2f8a12" d="M6.6 10.8a15.1 15.1 0 0 0 6.6 6.6l2.2-2.2c.3-.3.7-.4 1-.2 1.1.4 2.3.6 3.6.6.6 0 1 .4 1 1V20c0 .6-.4 1-1 1A17 17 0 0 1 3 4c0-.6.4-1 1-1h3.5c.6 0 1 .4 1 1 0 1.3.2 2.5.6 3.6.1.3 0 .7-.2 1z"/></svg>405-555-0192</li>
      <li><svg width="14" height="11" viewBox="0 0 30 22"><path fill="#2f8a12" d="M0 2a2 2 0 0 1 2-2h26a2 2 0 0 1 2 2v1L15 12 0 3z"/><path fill="#2f8a12" d="M0 6l15 9 15-9v14a2 2 0 0 1-2 2H2a2 2 0 0 1-2-2z"/></svg>info@brightmoor.com</li>
    </ul>
  </div>
  <div class="footer-col links">
    <h4>QUICK LINKS</h4>
    <ul><li>Home</li><li>About Us</li><li>What We Do</li><li>Commercial</li><li>Residential</li><li>Contact Us</li></ul>
  </div>
  <div class="footer-col signup">
    <h4>SIGN UP</h4>
    <div class="field">EMAIL ADDRESS</div>
    <div class="submit">SUBMIT NOW</div>
  </div>
  <div class="footer-art" role="img" aria-label="Illustration of an exterminator in a protective suit surrounded by crossed-out insect signs and spray bottles"></div>
</footer>

<div class="copyright">Brightmoor Pest Services PTY LTD. © 2021 All Rights Reserved.</div>

</div>
</body>
</html>
```